Hip Music Management Co. BIz Card

I have a logo (attached) the back side of the card should the full logo on the entire card- that's it. The front side of the card should show the logo somewhere, keeping with the 4 different shades of blue. The front side of the card can be a white background with logo and colored typeface for all info. Pretty simple.

Target Market(s)

I manage and produce a whole bunch of major label and indie artists.

Industry/Entity Type

Management

Contact Information for Business Card

Velmora Sound House (logo)
Dale Fornwick
President
www.velmorasoundhouse.com
dale@velmorasoundhouse.com
+1 310.555.7182
418 Willow Bend Lane
Ashgrove Falls, NY 10599

Requirements
Must have
• Entire logo on back side. White background on front- unless you provide something more interesting.
Nice to have
• On the front of the card if you choose a white backgound, if possible take my logo without the blue background (over white) that would be cool.

```html
<!DOCTYPE html>
<html lang="en">
<head>
<meta charset="utf-8">
<title>Velmora Sound House – Dale Fornwick</title>
<link rel="stylesheet" href="https://fonts.googleapis.com/css2?family=Jost:wght@500;600;700&display=swap">
<style>
  :root {
    --blue: #3d7cf5;
    --cyan: #7af4ff;
    --green: #6cf08a;
    --faint-cyan: #d6fbfd;
    --faint-green: #dcfde3;
    --paper: #ffffff;
    --shadow: rgba(0, 0, 0, 0.28);
  }
  * { margin: 0; padding: 0; box-sizing: border-box; }
  html, body {
    width: 1200px; height: 702px; overflow: hidden;
    background: var(--paper);
  }
  .card {
    position: relative;
    width: 1200px; height: 702px;
    overflow: hidden;
    background: var(--paper);
    font-family: "Jost", "Futura", sans-serif;
  }
  .accent-band {
    position: absolute;
    border-radius: 30px;
  }
  .accent-band--top {
    left: -120px; top: 40px;
    width: 760px; height: 90px;
    background: var(--faint-cyan);
    transform: rotate(-18deg);
  }
  .accent-band--bottom {
    left: 640px; top: 520px;
    width: 760px; height: 90px;
    background: var(--faint-green);
    transform: rotate(-25deg);
  }
  .address {
    position: absolute;
    left: 83px; top: 72px;
    font-style: normal;
    font-weight: 700;
    font-size: 18px;
    line-height: 35px;
    letter-spacing: 6px;
    color: var(--blue);
    text-shadow: 2px 2px 3px var(--shadow);
  }
  .brand-name {
    position: absolute;
    left: 855px; top: 86px;
    width: 260px;
    text-align: center;
    white-space: nowrap;
    font-weight: 700;
    font-size: 22px;
    line-height: 1.1;
    color: var(--blue);
  }
  .identity {
    position: absolute;
    left: 0; top: 164px;
    width: 1238px;
    text-align: center;
  }
  .person-first, .person-last {
    display: block;
    font-weight: 700;
    font-size: 116px;
    line-height: 124px;
    letter-spacing: -5px;
    text-shadow: 3px 3px 4px var(--shadow);
  }
  .person-first { color: var(--cyan); }
  .person-last { color: var(--blue); }
  .person-role {
    display: block;
    margin-top: -12px;
    font-weight: 600;
    font-size: 50px;
    line-height: 56px;
    letter-spacing: 24px;
    color: var(--green);
    text-shadow: 2px 2px 3px var(--shadow);
  }
  .contact {
    position: absolute;
    left: 0; top: 530px;
    width: 1240px;
    text-align: center;
    list-style: none;
    font-weight: 700;
    font-size: 16px;
    line-height: 30px;
    letter-spacing: 5.5px;
    color: var(--blue);
    text-shadow: 2px 2px 3px var(--shadow);
  }
</style>
</head>
<body>
  <main class="card">
    <span class="accent-band accent-band--top" aria-hidden="true"></span>
    <span class="accent-band accent-band--bottom" aria-hidden="true"></span>

    <address class="address">
      418 Willow Bend Lane<br>
      Ashgrove Falls<br>
      NY 10599
    </address>

    <div class="brand-name">Velmora Sound House</div>

    <h1 class="identity">
      <span class="person-first">Dale</span>
      <span class="person-last">Fornwick</span>
      <span class="person-role">President</span>
    </h1>

    <ul class="contact">
      <li>www.velmorasoundhouse.com</li>
      <li>dale@velmorasoundhouse.com</li>
      <li>+1 310.555.7182</li>
    </ul>
  </main>
</body>
</html>
```